Bright Pelvic Health Business Card

Need a business card for a surgical practice called Bright Pelvic Health. We have recently selected a logo (attached). The business card will need to have two formats:
1) One with the logo/physician name/ contact info on the front and location information on the back.
2) One in "appointment reminder card" style with the logo/ contact info/ date/ time on the front and the location information on the back.

The front side should include the following information:
- Logo
- Ravi K. Desai, MD FACOG
- phone: 469-555-0182
- fax: 1-469-555-0147
- email: admin@brightpelvic.example
- website: www.brightpelvichealth.example

The back side should have the office locations listed:
4812 Quarry Bend Dr, Plano, TX 75093
3650 Wrenfield Rd, Plano, TX 75025
2245 Brambleton Ln, Irving, TX 75038
915 S Garnet Ave B314, Dallas, TX 75201
1836 Tillman Pkwy, Grand Prairie, TX 75051
6417 Dorrance Way Dr, San Antonio, TX 78240
5920 Kessler Rd, Pasadena, TX 77504

Target Market(s)

1. Other physicians who might refer patients
2. Female patients

Industry/Entity Type

Business

Font styles to use
Other font styles liked:
• Tahoma for lettering

Requirements
Must have
• As per the instructions
Should not have
• No other images needed -- please try to keep font consistent with logo design. Can use Tahoma as the font for lettering.

```html
<!DOCTYPE html>
<html lang="en">
<head>
<meta charset="utf-8">
<title>Bright Pelvic Health – Business Card</title>
<link rel="stylesheet" href="https://fonts.googleapis.com/css2?family=Lato:wght@400;700&display=swap">
<style>
  :root {
    --bg: #ececec;
    --card: #fbfbfb;
    --brand-blue: #2b67a6;
    --ink: #1f1f1f;
    --panel-light: #8898cc;
    --panel-mid: #6b8cc4;
    --panel-deep: #3e7db6;
  }
  * { margin: 0; padding: 0; box-sizing: border-box; }
  html, body { width: 1200px; height: 720px; overflow: hidden; }
  body {
    background: var(--bg);
    font-family: "Lato", Tahoma, sans-serif;
    display: flex;
    align-items: center;
    justify-content: center;
    gap: 60px;
  }
  .card {
    position: relative;
    width: 540px;
    height: 309px;
    background: var(--card);
    border: 1px solid #dcdcdc;
    overflow: hidden;
  }
  .portrait-panel {
    position: absolute;
    top: 0;
    height: 100%;
    width: 185px;
  }
  .card-front .portrait-panel {
    right: 0;
    background: linear-gradient(90deg, var(--panel-light) 0%, var(--panel-mid) 45%, var(--panel-deep) 100%);
  }
  .card-back .portrait-panel {
    left: 0;
    width: 170px;
    background: linear-gradient(90deg, var(--panel-deep) 0%, var(--panel-mid) 55%, var(--panel-light) 100%);
  }
  .brand {
    position: absolute;
    left: 34px;
    top: 76px;
    display: flex;
    align-items: center;
    gap: 8px;
    color: var(--brand-blue);
    font-weight: 700;
    font-size: 21px;
    letter-spacing: 0.2px;
  }
  .brand-dot {
    width: 12px; height: 12px;
    border-radius: 50%;
    background: var(--brand-blue);
  }
  .physician {
    position: absolute;
    left: 35px;
    top: 130px;
    color: var(--brand-blue);
  }
  .physician-name { font-size: 17px; font-weight: 700; line-height: 1.2; }
  .physician-title { font-size: 12px; color: var(--ink); line-height: 1.2; }
  .contact-list {
    position: absolute;
    left: 35px;
    top: 196px;
    list-style: none;
    font-size: 12.5px;
    color: var(--ink);
  }
  .contact-list li {
    display: flex;
    align-items: center;
    gap: 9px;
    height: 16.5px;
  }
  .contact-list svg { width: 13px; height: 11px; fill: var(--brand-blue); flex: none; }
  .locations {
    position: absolute;
    right: 21px;
    top: 56px;
    text-align: right;
    color: var(--ink);
  }
  .locations-heading {
    font-size: 16.5px;
    font-weight: 700;
    color: var(--brand-blue);
    line-height: 25.7px;
  }
  .locations-list { list-style: none; font-size: 16.5px; line-height: 25.7px; }
</style>
</head>
<body>

  <section class="card card-front">
    <div class="brand"><span class="brand-dot"></span>Bright Pelvic Health</div>
    <div class="physician">
      <div class="physician-name">Ravi K. Desai</div>
      <div class="physician-title">MD FACOG</div>
    </div>
    <ul class="contact-list">
      <li>
        <svg viewBox="0 0 13 11" aria-hidden="true"><path d="M1 3.5C1 1.5 3 1 6.5 1S12 1.5 12 3.5L10 4.2 9 2.8H4L3 4.2Z"/><path d="M3.5 5h6l1.5 5H2Z"/></svg>
        469-555-0182
      </li>
      <li>
        <svg viewBox="0 0 13 11" aria-hidden="true"><rect x="3" y="0.5" width="7" height="3"/><rect x="0.5" y="4" width="12" height="4.5" rx="1"/><rect x="3" y="7" width="7" height="3.5" fill="#fff" stroke="#2b67a6" stroke-width="1"/></svg>
        1-469-555-0147
      </li>
      <li>
        <svg viewBox="0 0 13 11" aria-hidden="true"><rect x="0.5" y="1" width="12" height="9"/><path d="M1 1.5l5.5 4.5 5.5-4.5" fill="none" stroke="#fff" stroke-width="1"/></svg>
        admin@brightpelvic.example
      </li>
      <li>
        <svg viewBox="0 0 13 11" aria-hidden="true"><path d="M0.5 0.5h12v8h-12Zm1.5 1.5v5h9v-5Z"/><rect x="4" y="9.2" width="5" height="1.3"/></svg>
        www.brightpelvichealth.example
      </li>
    </ul>
    <div class="portrait-panel" role="img" aria-label="Blue side-profile silhouette of a woman"></div>
  </section>

  <section class="card card-back">
    <div class="portrait-panel" role="img" aria-label="Blue side-profile silhouette of a woman, mirrored"></div>
    <div class="locations">
      <div class="locations-heading">Office locations :</div>
      <ul class="locations-list">
        <li>4812 Quarry Bend Dr, Plano, TX 75093</li>
        <li>3650 Wrenfield Rd, Plano, TX 75025</li>
        <li>2245 Brambleton Ln, Irving, TX 75038</li>
        <li>915 S Garnet Ave B314, Dallas, TX 75201</li>
        <li>1836 Tillman Pkwy, Grand Prairie, TX 75051</li>
        <li>6417 Dorrance Way Dr, San Antonio, TX 78240</li>
        <li>5920 Kessler Rd, Pasadena, TX 77504</li>
      </ul>
    </div>
  </section>

</body>
</html>
```